Church needs a graphic design/flyer layout for upcoming series

I need a multi-purpose design for promoting both our upcoming series of messages and our fall kick-off event where we will launch the messages.

Our promotion will be printed on a two-sided. One side is simple and focuses on the series and the other side has details in regards to the event. I have provided an attachment example of what we did last time.

The design needs to be multi-purpose because it will be used for our sermon Power Points, placed on our website banner, social media, etc.

• Sermon series is called “Harbor Lanterns”
• The subtitle will be “What’s keeping you from God?”
• Our name logo should be on the graphic as well.
• The subject manner will revolve around common hurdles that people face about God and Christianity: The existence of God, the exclusivity of religion, Hell, the reliability of the Bible, Hypocrisy in the church, etc.
• Our mission is “Connecting Young Families to Christ” so our focus is to reach out to families while not being exclusive to others.
• Our target audience is families with school-aged kids.
• This series is an invitational focus so we want it to be appealing to non-church goers.
• It should be attention grabbing while not being too ‘edgy’

• The front of the card will most likely consist the Sermon Series Graphic, title & subtitle of the series, and perhaps our name logo somewhere on it.
• The back of the card will invite and give the basic information for the event so that the people will be encouraged to save the date and come to the event.
• Here are some things that could be included on that advertisement:
o The name of the event: “Westbrook Commons Open Day”
o The date and time of the event: Sept 23rd @ 10:30
o Features of the event:
 Free lunch
 Children’s program
 Bouncy Castle
 Start of the “Harbor Lanterns” messages.
 Sample of topics
o Information about the church: our website and address, etc
o Engaging pictures and graphics.
• The rest of the tone and manner are the same as the sermon series graphic.
The flyer will be 11X14, like a postcard size.

Target Market(s)

Young families who are spiritually curious but not committed church attenders.

Colors

Designer to choose colors to be used in the design.

Requirements
Nice to have
• A modern and professional looking design.
Should not have
• Anything offensive or not family friendly.

```html
<!DOCTYPE html>
<html lang="en">
<head>
<meta charset="utf-8">
<title>Harbor Lanterns – Flyer</title>
<link rel="stylesheet" href="https://fonts.googleapis.com/css2?family=Chewy&family=Arimo:wght@400;700&display=swap">
<style>
  :root {
    --backdrop: #a9adb6;
    --card-shadow: rgba(20, 24, 36, 0.45);
    --night: #2a2f45;
    --slate: #434b66;
    --slate-light: #56607c;
    --orange: #f7a21b;
    --orange-dark: #e8891a;
    --purple: #8a2a9a;
    --ink: #1d1d24;
    --white: #ffffff;
    --soft-white: #e4e7ef;
  }
  * { margin: 0; padding: 0; box-sizing: border-box; }
  html, body {
    width: 1200px; height: 2298px; overflow: hidden;
    background: var(--backdrop);
    font-family: "Arimo", Arial, sans-serif;
  }
  .canvas { position: relative; width: 1200px; height: 2298px; }

  .card {
    position: absolute; left: 100px; width: 1000px; height: 781px;
    overflow: hidden;
    box-shadow: 0 14px 36px var(--card-shadow);
  }
  .card--front { top: 300px; }
  .card--back { top: 1220px; background: var(--slate); }

  /* Front */
  .series-art {
    position: absolute; inset: 0;
    background:
      radial-gradient(circle at 49% 12%, #ffffff 0, #e9eef8 9%, rgba(180,196,226,0.6) 20%, rgba(90,100,150,0) 38%),
      linear-gradient(160deg, #2d3f6e 0%, #5d6ea3 30%, #6d5a9b 55%, #3e3656 78%, #151320 100%);
  }
  .series-art::after {
    content: ""; position: absolute; right: 0; top: 0; width: 45%; height: 40%;
    background: radial-gradient(ellipse at 100% 30%, rgba(214,110,170,0.55), rgba(214,110,170,0) 70%);
  }
  .series-frame { position: absolute; left: 58px; top: 58px; width: 884px; height: 560px; }
  .series-title {
    position: absolute; left: 0; right: 0; top: 470px;
    text-align: center;
    font-family: "Chewy", cursive;
    font-size: 96px; line-height: 1; letter-spacing: 1px;
    color: var(--orange);
    -webkit-text-stroke: 3px var(--ink);
    paint-order: stroke fill;
    text-shadow: 0 0 6px var(--white), 0 0 2px var(--white);
  }
  .series-subtitle {
    position: absolute; left: 0; right: 0; top: 600px;
    text-align: center;
    font-weight: 700; font-size: 39px;
    color: var(--white);
    -webkit-text-stroke: 6px var(--ink);
    paint-order: stroke fill;
  }

  /* Back */
  .event-rays {
    position: absolute; inset: 0;
    background:
      radial-gradient(circle at 52% 48%, var(--slate-light) 0, var(--slate) 45%, var(--night) 100%);
  }
  .event-title {
    position: absolute; left: 0; right: 0; top: 82px;
    text-align: center;
    font-family: "Chewy", cursive;
    font-size: 62px; line-height: 1;
    color: var(--purple);
    -webkit-text-stroke: 6px var(--white);
    paint-order: stroke fill;
  }
  .event-date { position: absolute; left: 262px; top: 150px; width: 530px; height: 62px; }
  .event-date-text {
    position: absolute; left: 262px; top: 150px; width: 500px; height: 56px;
    display: flex; align-items: center; justify-content: center;
    font-weight: 700; font-size: 39px; color: var(--ink);
  }
  .features-heading {
    position: absolute; left: 72px; top: 306px;
    font-weight: 700; font-size: 33px; color: var(--white);
  }
  .features-list { position: absolute; left: 72px; top: 362px; list-style: none; }
  .features-list li {
    position: relative; padding-left: 36px;
    font-size: 29px; line-height: 46.5px; color: var(--soft-white);
  }
  .features-list li::before {
    content: ""; position: absolute; left: 2px; top: 15px;
    width: 17px; height: 17px; border-radius: 50%; background: var(--orange);
  }
  .church-name {
    position: absolute; left: 670px; top: 408px; width: 270px;
    display: flex; flex-direction: column; align-items: center; gap: 16px;
  }
  .church-name-dot { width: 120px; height: 120px; border-radius: 50%; background: var(--orange); }
  .church-name-text { font-size: 25px; color: var(--white); text-align: center; }
  .event-rule { position: absolute; left: 72px; top: 634px; width: 856px; height: 2px; background: var(--soft-white); }
  .event-contact {
    position: absolute; left: 0; right: 0; top: 652px;
    text-align: center; font-size: 25px; line-height: 36px; color: var(--soft-white);
  }
</style>
</head>
<body>
<main class="canvas">

  <section class="card card--front" aria-label="Series card, front">
    <div class="series-art" role="img" aria-label="Moonlit mountain range at dusk with a dark rough cross and a faint question mark in the sky"></div>
    <svg class="series-frame" viewBox="0 0 884 560" aria-hidden="true">
      <defs>
        <linearGradient id="frameFade" x1="0" y1="0" x2="0" y2="1">
          <stop offset="0" stop-color="#fff" stop-opacity="0.85"/>
          <stop offset="0.75" stop-color="#fff" stop-opacity="0.6"/>
          <stop offset="1" stop-color="#fff" stop-opacity="0"/>
        </linearGradient>
      </defs>
      <path d="M2 560 V2 H882 V560" fill="none" stroke="url(#frameFade)" stroke-width="4"/>
    </svg>
    <h1 class="series-title">Harbor Lanterns</h1>
    <p class="series-subtitle">What’s keeping you from God?</p>
  </section>

  <section class="card card--back" aria-label="Event card, back">
    <div class="event-rays" role="img" aria-label="Soft slate sunburst background"></div>
    <h2 class="event-title">Westbrook Commons Open Day</h2>
    <svg class="event-date" viewBox="0 0 530 62" aria-hidden="true">
      <polygon points="14,6 500,0 482,28 530,56 8,62 0,30" fill="var(--orange-dark)"/>
      <polygon points="18,8 496,3 480,28 520,53 12,56 4,30" fill="var(--orange)"/>
    </svg>
    <p class="event-date-text">Sept. 23rd @ 10:30</p>

    <h3 class="features-heading">Features of the event:</h3>
    <ul class="features-list">
      <li>Free lunch</li>
      <li>Children’s program</li>
      <li>Bouncy Castle</li>
      <li>Start of the “Harbor Lanterns” messages.</li>
      <li>Sample of topics</li>
    </ul>

    <div class="church-name">
      <span class="church-name-dot" aria-hidden="true"></span>
      <span class="church-name-text">Westbrook Commons Church</span>
    </div>

    <div class="event-rule"></div>
    <p class="event-contact">
      Location: 1185 Alder Ridge Road, Brookvale, ON K0L 2B4<br>
      P: 555 014 2290 | E: hello@westbrookcommons.ca | W: www.westbrookcommons.ca
    </p>
  </section>

</main>
</body>
</html>
```